Harborline Quoting
Business Cards and Stationery for Service Co
Simple
Dane Corwell
Vice President
20436 SW 47th Avenue Suite 3105 Vancouver, WA 97531
danec@harborlinequoting.com
www.harborlinequoting.com
Please keep it simple and professional.
Just the logo

```html
<!DOCTYPE html>
<html lang="en">
<head>
<meta charset="utf-8">
<title>Harborline Quoting — Business Cards</title>
<link rel="stylesheet" href="https://fonts.googleapis.com/css2?family=Montserrat:wght@400;600;700&display=swap">
<style>
  :root {
    --brand-orange: #e0561f;
    --brand-orange-deep: #c9481a;
    --card-white: #ffffff;
    --ink: #4a4a4a;
    --ink-soft: #7a7a7a;
    --backdrop: #ece9e4;
  }
  * { margin: 0; padding: 0; box-sizing: border-box; }
  html, body {
    width: 1200px; height: 901px; overflow: hidden;
    background: var(--backdrop);
    font-family: "Montserrat", Arial, sans-serif;
  }
  .sheet {
    width: 1200px; height: 901px;
    display: flex; align-items: center; justify-content: center; gap: 60px;
  }
  .card {
    position: relative; width: 520px; height: 297px; overflow: hidden;
    box-shadow: 0 6px 18px rgba(0,0,0,.12);
  }
  .card-back { background: var(--brand-orange); color: var(--card-white); }
  .card-front { background: var(--card-white); color: var(--ink); }

  .deco-circle { position: absolute; border-radius: 50%; }
  .card-back .deco-circle { width: 300px; height: 300px; left: -70px; top: 60px; background: var(--card-white); }
  .card-front .deco-circle { width: 230px; height: 230px; left: -60px; top: 150px; background: var(--brand-orange); }

  .wordmark {
    position: absolute; display: flex; align-items: center; gap: 10px;
    font-weight: 700; letter-spacing: .08em; text-transform: uppercase; line-height: 1.1;
  }
  .wordmark-dot { width: 30px; height: 30px; border-radius: 50%; flex: none; }
  .card-back .wordmark { right: 34px; top: 112px; font-size: 22px; color: var(--card-white); }
  .card-back .wordmark-dot { background: var(--card-white); }
  .card-front .wordmark { left: 200px; top: 38px; font-size: 21px; color: var(--brand-orange); }
  .card-front .wordmark-dot { background: var(--brand-orange); }

  .back-url {
    position: absolute; left: 250px; bottom: 26px;
    font-size: 11px; letter-spacing: .04em; color: var(--card-white);
  }

  .contact { position: absolute; left: 200px; top: 118px; }
  .contact-name { font-size: 20px; font-weight: 400; color: var(--brand-orange); }
  .contact-title { font-size: 10px; color: var(--ink-soft); margin-bottom: 10px; }
  .contact-line { display: flex; align-items: center; gap: 7px; font-size: 10.5px; margin-bottom: 4px; }
  .contact-line svg { width: 10px; height: 10px; fill: var(--brand-orange); flex: none; }

  .front-band {
    position: absolute; left: 0; right: 0; bottom: 0; height: 30px;
    background: var(--brand-orange);
    display: flex; align-items: center; padding-left: 200px;
    font-size: 11px; font-weight: 600; letter-spacing: .04em; color: var(--card-white);
  }
</style>
</head>
<body>
<main class="sheet">
  <section class="card card-back" aria-label="Card back">
    <div class="deco-circle"></div>
    <div class="wordmark"><span class="wordmark-dot"></span><span>Harborline<br>Quoting</span></div>
    <p class="back-url">www.harborlinequoting.com</p>
  </section>

  <section class="card card-front" aria-label="Card front">
    <div class="deco-circle"></div>
    <div class="wordmark"><span class="wordmark-dot"></span><span>Harborline<br>Quoting</span></div>
    <div class="contact">
      <h1 class="contact-name">Dane Corwell</h1>
      <p class="contact-title">Vice President</p>
      <p class="contact-line"><svg viewBox="0 0 10 10"><path d="M2 0h2l1 2.5-1.3 1a5 5 0 0 0 2.8 2.8l1-1.3L10 6v2a2 2 0 0 1-2 2A8 8 0 0 1 0 2a2 2 0 0 1 2-2z"/></svg>360-555-0142</p>
      <p class="contact-line"><svg viewBox="0 0 10 10"><path d="M2 0h2l1 2.5-1.3 1a5 5 0 0 0 2.8 2.8l1-1.3L10 6v2a2 2 0 0 1-2 2A8 8 0 0 1 0 2a2 2 0 0 1 2-2z"/></svg>888-555-0187</p>
      <p class="contact-line"><svg viewBox="0 0 10 10"><path d="M0 1.5h10v7H0z M0 1.5l5 4 5-4" /></svg>danec@harborlinequoting.com</p>
    </div>
    <div class="front-band">www.harborlinequoting.com</div>
  </section>
</main>
</body>
</html>
```